Mini Market Tavo Business Presentation Cards

We need presentation cards with a logo we already own designed at this website as well. We need the printing, delivery and sleek, modem design in harmony with our previous logo design.

Target Market(s)

Low, med and High income class.

Industry/Entity Type

Grocery Store

Contact Information for Business Card

Business logo (Mini Market Tavo), name: Esteban L. Morales/Lidia M. Paz/ Hugo Paz (those are the names for the different cards),
Address: Col. Lomas del Viento, carretera a Tela a 200mts del Centro Comunal. Villa Marina, Costa Norte.
Email: minimarkettavo@correo-ejemplo.hn
Teléfono: (504) 9731-5064

Font styles to use
Serif
Sans Serif

Requirements
Must have
• Business logo (Mini Market Tavo), person name, department,
• Address, phone number, email address.

```html
<!DOCTYPE html>
<html lang="es">
<head>
<meta charset="utf-8">
<title>Mini Market Tavo – Tarjeta de presentación</title>
<link rel="stylesheet" href="https://fonts.googleapis.com/css2?family=Noto+Serif:wght@400;700&family=Open+Sans:wght@400&display=swap">
<style>
  :root {
    --page: #ecebe7;
    --card-white: #ffffff;
    --card-haze: #f4f6f0;
    --green-light: #b9dc7a;
    --green-dark: #6faa3a;
    --orange: #e8593a;
    --ink: #161616;
  }
  * { margin: 0; padding: 0; box-sizing: border-box; }
  html, body {
    width: 1200px; height: 892px; overflow: hidden;
    background: var(--page);
  }
  .canvas {
    position: relative; width: 1200px; height: 892px;
    display: flex; align-items: center; justify-content: center;
  }
  .card {
    position: relative; width: 1000px; height: 572px;
    border-radius: 34px; overflow: hidden;
    box-shadow: 0 10px 30px rgba(0,0,0,.18);
    background: var(--green-dark);
  }
  .card-shapes { position: absolute; inset: 0; }
  .brand-name {
    position: absolute; left: 70px; top: 80px;
    font-family: "Noto Serif", serif; font-weight: 400;
    font-size: 64px; line-height: 1; color: var(--ink);
    white-space: nowrap;
  }
  .person {
    position: absolute; left: 110px; top: 250px;
    font-family: "Noto Serif", serif; font-weight: 700;
    font-size: 34px; line-height: 1.2; color: var(--ink);
    white-space: nowrap;
  }
  .contact {
    position: absolute; font-family: "Open Sans", sans-serif;
    font-size: 22px; line-height: 1.3; color: var(--ink);
    display: flex; align-items: center; gap: 14px; white-space: nowrap;
  }
  .contact svg { width: 18px; height: 18px; flex: none; }
  .contact-email { right: 60px; top: 392px; }
  .contact-address { left: 270px; top: 448px; display: block; line-height: 1.55; }
  .contact-phone { left: 60px; top: 522px; }
</style>
</head>
<body>
<main class="canvas">
  <article class="card">
    <svg class="card-shapes" viewBox="0 0 1000 572" preserveAspectRatio="none" aria-hidden="true">
      <defs>
        <linearGradient id="greenField" x1="0" y1="1" x2="1" y2="0">
          <stop offset="0" stop-color="#6faa3a"/>
          <stop offset=".55" stop-color="#b9dc7a"/>
          <stop offset="1" stop-color="#6faa3a"/>
        </linearGradient>
      </defs>
      <rect width="1000" height="572" fill="url(#greenField)"/>
      <path d="M0,0 H790 C760,200 560,400 0,470 Z" fill="#f4f6f0"/>
      <path d="M0,0 H760 C730,190 540,380 0,455 Z" fill="#ffffff"/>
      <path d="M0,462 C560,392 765,200 800,0" fill="none" stroke="#e8593a" stroke-width="9"/>
    </svg>

    <h1 class="brand-name">Mini Market Tavo</h1>

    <p class="person">Esteban L. Morales</p>

    <p class="contact contact-email">
      minimarkettavo@correo-ejemplo.hn
      <svg viewBox="0 0 18 18"><rect x="1" y="3" width="16" height="12" rx="2" fill="#161616"/><path d="M2 4 L9 10 L16 4" stroke="#fff" stroke-width="1.5" fill="none"/></svg>
    </p>

    <p class="contact contact-address">
      Col. Lomas del Viento, carretera a Tela a<br>
      200mts del Centro Comunal. Villa Marina, Costa Norte.
    </p>

    <p class="contact contact-phone">
      <svg viewBox="0 0 18 18"><rect x="0" y="0" width="18" height="18" rx="3" fill="#161616"/><path d="M5 4 C4 9 9 14 14 13 L14 11 L11.5 10 L10.5 11 C8.5 10 8 9.5 7 7.5 L8 6.5 L7 4 Z" fill="#fff"/></svg>
      (504) 9731-5064
    </p>
  </article>
</main>
</body>
</html>
```